Roofing Company Sales Rep Business Card

Business card for sales rep to canvass and hand out to property owners/managers for free roof inspections and roof replacements.

```html
<!DOCTYPE html>
<html lang="en">
<head>
<meta charset="UTF-8">
<title>Ridgeline Roofing – Sales Rep Business Card</title>
<link rel="stylesheet" href="https://fonts.googleapis.com/css2?family=Questrial&display=swap">
<style>
  :root {
    --backdrop: #3b4040;
    --card: #ffffff;
    --brand-red: #ec1c24;
    --ink: #1c1c1c;
    --muted: #555555;
    --band-text: #ffffff;
  }
  * { margin: 0; padding: 0; box-sizing: border-box; }
  html, body {
    width: 1200px;
    height: 1000px;
    overflow: hidden;
    background: var(--backdrop);
    font-family: "Questrial", sans-serif;
    color: var(--ink);
  }
  .canvas { position: relative; width: 1200px; height: 1000px; }

  .card { position: absolute; background: var(--card); }

  /* Front side */
  .card-front { left: 213px; top: 163px; width: 573px; height: 316px; }
  .card-front .brand {
    position: absolute; left: 0; right: 0; top: 130px;
    display: flex; align-items: center; justify-content: center; gap: 14px;
  }
  .brand-mark { width: 26px; height: 26px; background: var(--brand-red); border-radius: 50%; flex: none; }
  .brand-name { font-size: 36px; color: var(--ink); letter-spacing: 1px; white-space: nowrap; }
  .web-band {
    position: absolute; left: 0; bottom: 0; width: 100%; height: 32px;
    background: var(--brand-red); color: var(--band-text);
    display: flex; align-items: center; justify-content: center;
    font-size: 17px; letter-spacing: 5px;
  }

  /* Back side */
  .card-back { left: 419px; top: 518px; width: 584px; height: 334px; }
  .rep { position: absolute; left: 39px; top: 40px; }
  .rep-name { font-size: 19px; letter-spacing: 1px; }
  .rep-title { font-size: 14px; color: var(--muted); margin-top: 4px; letter-spacing: 0.5px; }
  .card-back .brand {
    position: absolute; left: 40px; top: 150px;
    display: flex; align-items: center; gap: 10px;
  }
  .card-back .brand-mark { width: 18px; height: 18px; }
  .card-back .brand-name { font-size: 24px; letter-spacing: 0.5px; }
  .offer {
    position: absolute; left: 40px; top: 196px;
    font-size: 14px; color: var(--brand-red); letter-spacing: 0.5px; line-height: 20px;
  }
  .address {
    position: absolute; left: 299px; top: 45px;
    font-style: normal; font-size: 17.5px; line-height: 34.5px; letter-spacing: 0.3px;
  }
  .contacts { position: absolute; left: 299px; top: 195px; list-style: none; font-size: 18px; }
  .contacts li { display: flex; align-items: center; gap: 8px; height: 30.5px; white-space: nowrap; }
  .contacts svg { width: 16px; height: 16px; flex: none; }
</style>
</head>
<body>
<main class="canvas">
  <section class="card card-front" aria-label="Business card front">
    <div class="brand">
      <span class="brand-mark"></span>
      <span class="brand-name">Ridgeline Roofing</span>
    </div>
    <div class="web-band">ridgelineroofing.com</div>
  </section>

  <section class="card card-back" aria-label="Business card back">
    <div class="rep">
      <p class="rep-name">Jordan Ellis</p>
      <p class="rep-title">Sales Representative</p>
    </div>
    <div class="brand">
      <span class="brand-mark"></span>
      <span class="brand-name">Ridgeline Roofing</span>
    </div>
    <p class="offer">Free roof inspections<br>&amp; replacement quotes</p>
    <address class="address">
      418 Cedar Hollow Road<br>
      Suite 12, Harlow Springs<br>
      North Carolina 28011
    </address>
    <ul class="contacts">
      <li>
        <svg viewBox="0 0 24 24" aria-hidden="true"><path fill="#1c1c1c" d="M6.6 10.8a15.1 15.1 0 0 0 6.6 6.6l2.2-2.2c.3-.3.7-.4 1-.2 1.1.4 2.3.6 3.6.6.6 0 1 .4 1 1V20c0 .6-.4 1-1 1A17 17 0 0 1 3 4c0-.6.4-1 1-1h3.5c.6 0 1 .4 1 1 0 1.3.2 2.5.6 3.6.1.3 0 .7-.2 1z"/></svg>
        (555) 014-2270
      </li>
      <li>
        <svg viewBox="0 0 24 24" aria-hidden="true"><rect x="2" y="5" width="20" height="14" fill="#1c1c1c"/><path d="M3 6l9 7 9-7" fill="none" stroke="#fff" stroke-width="1.6"/></svg>
        jo@ridgelineroofing.com
      </li>
      <li>
        <svg viewBox="0 0 24 24" aria-hidden="true" fill="none" stroke="#1c1c1c" stroke-width="1.8"><circle cx="12" cy="12" r="10"/><ellipse cx="12" cy="12" rx="4.5" ry="10"/><path d="M2 12h20M4 7h16M4 17h16"/></svg>
        www.ridgelineroofing.com
      </li>
    </ul>
  </section>
</main>
</body>
</html>
```